Brenford Works Business Card

Modern and Professional Business Card for a Med size construction/development company.

See the samples below for the design I like … but I need ideas for incorporating the red company logo while still keeping the clean look of the card samples that are attached.

Logo and tag line on the back … info on the front.

Tagline: Built Right from the Footings Up

Target Market(s)

Med-Large General Contractors

Contact Information for Business Card

Brenford Works Limited
42 Marsh Lane
Mt. Pearl, NL
A1N 6T2

t: 555-555-0142
f: 555-555-0187
w: www.brenfordworks.example

Font styles to use
Sans Serif

Colors
fbee3e

Requirements
Must have
• I like the black and yellow designs of the attached samples …. but I'm not sure how to incorporate the red Brenford Works logo into that design??
Nice to have
• Construction safety strips

```html
<!DOCTYPE html>
<html lang="en">
<head>
<meta charset="utf-8">
<title>Brenford Works Business Card</title>
<link rel="stylesheet" href="https://fonts.googleapis.com/css2?family=Arvo:wght@400;700&display=swap">
<style>
  :root {
    --yellow: #f8ec42;
    --accent-yellow: #fbee3e;
    --black: #0b0b0b;
    --red: #e62226;
    --white: #ffffff;
    --page: #eeeeee;
  }
  html, body {
    margin: 0;
    padding: 0;
    width: 1200px;
    height: 923px;
    overflow: hidden;
    background: var(--page);
    font-family: "Arvo", Georgia, serif;
  }
  .canvas { position: relative; width: 1200px; height: 923px; }
  .card {
    position: absolute;
    left: 290px;
    width: 621px;
    height: 354px;
    overflow: hidden;
    box-shadow: 0 6px 18px rgba(0,0,0,0.18);
  }
  /* Logo side */
  .card--logo { top: 83px; background: var(--yellow); }
  .wordmark {
    position: absolute;
    left: 0; right: 0;
    top: 112px;
    text-align: center;
    color: var(--red);
    font-weight: 700;
    font-size: 48px;
    line-height: 1.1;
    letter-spacing: 1px;
  }
  .wordmark__sub { display: block; margin-top: 10px; font-size: 26px; letter-spacing: 6px; }
  .tagline-band {
    position: absolute;
    left: 0; right: 0;
    top: 303px;
    height: 29px;
    background: var(--black);
    color: var(--accent-yellow);
    font-size: 15.5px;
    line-height: 29px;
    text-align: center;
    text-transform: uppercase;
  }
  /* Info side */
  .card--info { top: 485px; background: var(--black); }
  .info-mark {
    position: absolute;
    right: 40px;
    top: 34px;
    text-align: center;
    color: var(--red);
    font-weight: 700;
    font-size: 36px;
    line-height: 1.1;
    letter-spacing: 1px;
  }
  .info-mark__sub { display: block; margin-top: 8px; font-size: 20px; letter-spacing: 5px; }
  .person { position: absolute; left: 40px; top: 158px; }
  .person__name { color: var(--accent-yellow); font-size: 25px; line-height: 30px; }
  .person__role { color: var(--white); font-size: 15px; line-height: 18px; }
  .divider {
    position: absolute;
    left: 41px; right: 41px;
    top: 221px;
    height: 1.5px;
    background: var(--accent-yellow);
  }
  .contacts {
    position: absolute;
    left: 40px;
    top: 241px;
    margin: 0; padding: 0;
    list-style: none;
    color: var(--white);
    font-size: 17px;
  }
  .contacts li { display: flex; align-items: center; height: 26px; }
  .contacts svg { width: 20px; height: 20px; margin-right: 12px; fill: var(--accent-yellow); }
  .address {
    position: absolute;
    right: 39px;
    top: 241px;
    text-align: right;
    font-style: normal;
    color: var(--white);
    font-size: 17px;
    line-height: 26px;
  }
  .address__company { color: var(--accent-yellow); }
  .safety-strip { position: absolute; left: 0; bottom: 0; width: 621px; height: 11px; }
</style>
</head>
<body>
<div class="canvas">

  <section class="card card--logo">
    <div class="wordmark">BRENFORD WORKS<span class="wordmark__sub">LIMITED</span></div>
    <div class="tagline-band">Built right from the footings up</div>
  </section>

  <section class="card card--info">
    <div class="info-mark">BRENFORD WORKS<span class="info-mark__sub">LIMITED</span></div>

    <div class="person">
      <div class="person__name">John Doe</div>
      <div class="person__role">Contractor</div>
    </div>

    <div class="divider"></div>

    <ul class="contacts">
      <li>
        <svg viewBox="0 0 24 24" aria-hidden="true"><path d="M3 9c0-3 4-5 9-5s9 2 9 5l-1 2-4-1V8c-2-.6-6-.6-8 0v2l-4 1zM6 12h12l2 8H4zm6 2a2.5 2.5 0 100 5 2.5 2.5 0 000-5z"/></svg>
        555 - 555 - 0142
      </li>
      <li>
        <svg viewBox="0 0 24 24" aria-hidden="true"><path d="M2 9h4v12H2zM7 7h3V3h9v4h3v14H7zm4-2v2h6V5zm1 6v2h2v-2zm4 0v2h2v-2zm-4 4v2h2v-2zm4 0v2h2v-2z"/></svg>
        555 - 555 - 0187
      </li>
      <li>
        <svg viewBox="0 0 24 24" aria-hidden="true"><path d="M12 2a10 10 0 100 20 10 10 0 000-20zm0 2c1 0 2 .3 3 .8-.5.8-1.5 1-2 2s0 2-1 2.5-2 0-2.5 1 .5 2 1.5 2.5 1 2 .5 3-1 2.5-1.5 3.7A8 8 0 015 8c1 0 1.5 1 2.5 1S9 7 9 6s1-2 3-2zm5 3.5a8 8 0 011.5 9c-.5-1-1.5-1-2-2s.5-2 0-3-1.5-1-1.5-2 1-1.5 2-2z"/></svg>
        www.brenfordworks.example
      </li>
    </ul>

    <address class="address">
      <div class="address__company">Brenford Works Limited</div>
      <div>42 Marsh Lane</div>
      <div>Marlow Cove, QC, J9X 6T2</div>
    </address>

    <svg class="safety-strip" viewBox="0 0 621 11" aria-hidden="true">
      <rect x="0" y="0" width="621" height="11" fill="var(--accent-yellow)"/>
      <polygon points="418,11 422,0 621,0 621,11" fill="var(--black)"/>
      <polygon points="424,11 428,0 621,0 621,11" fill="var(--red)"/>
    </svg>
  </section>

</div>
</body>
</html>
```